Bref créative
Stationary and Business Cards Orla Ridge Capital
Stationary, Envelopes, Business Cards
Professional
Marcus Bellwin
Managing Partner
8734 Fernhollow Ave. Suite 4580
Los Angeles, CA 90217
marcus@orlaridgecapital.example
orlaridgecapital.example
Design should be similar to the informational side of the business card (with bull silhouette) I had designed previously (uploaded), but with colors matching my website colors of black+white+blue (see previous contest and also uploaded).
Should contain the following:
-Company Logo (uploaded)
-The Slogan "Hedge Fund Strategies at Mutual Fund Prices"
-And the offer "Free Financial Check-Up"
Here is the previous business card. I don't care about the pattern in the background as that didn't show up in printing anyway.
here is a draft version of the website, to give you an idea of the general appearance
here is the company logo

```html
<!DOCTYPE html>
<html lang="en">
<head>
<meta charset="utf-8">
<title>Orla Ridge Capital – Business Cards</title>
<link href="https://fonts.googleapis.com/css2?family=Arimo:ital,wght@0,400;0,700;1,700&display=swap" rel="stylesheet">
<style>
  :root {
    --page: #e9e9e9;
    --card-black: #050505;
    --blue: #1aa3d6;
    --blue-light: #4cc3ea;
    --blue-deep: #0a6f98;
    --white: #ffffff;
  }
  * { box-sizing: border-box; margin: 0; padding: 0; }
  html, body { width: 1200px; height: 802px; overflow: hidden; }
  body { background: var(--page); font-family: "Arimo", Arial, sans-serif; position: relative; }

  .card {
    position: absolute; width: 458px; height: 295px; border-radius: 14px;
    background: var(--card-black); overflow: hidden;
    box-shadow: 0 3px 10px rgba(0,0,0,.25);
  }
  .card--front-swoosh { left: 137px; top: 96px; }
  .card--front-plain { left: 619px; top: 96px; }
  .card--back-dark { left: 137px; top: 413px; }
  .card--back-blue { left: 619px; top: 413px;
    background: linear-gradient(180deg, var(--blue-deep) 0%, var(--blue-light) 30%, #f4fbfe 55%, var(--blue-light) 80%, var(--blue-deep) 100%); }

  .swoosh-area {
    position: absolute; left: 0; top: 40px; width: 140px; height: 110px;
    background: linear-gradient(45deg, var(--blue-deep) 0%, var(--blue) 55%, var(--blue-light) 100%);
    opacity: .85; border-top-right-radius: 40px; border-bottom-right-radius: 40px;
  }

  .brand { position: absolute; display: flex; align-items: center; gap: 10px; }
  .card--front-swoosh .brand { left: 148px; top: 28px; }
  .card--front-plain .brand { left: 26px; top: 28px; }
  .brand__mark { width: 64px; height: 64px; background: var(--blue); }
  .brand__name { color: var(--white); font-size: 22px; font-weight: 700; letter-spacing: 1px; }

  .person { position: absolute; left: 14px; top: 200px; }
  .person__name { color: var(--blue); font-size: 15px; font-weight: 700; }
  .person__title { color: var(--white); font-size: 12px; margin-top: 3px; }

  .contact { position: absolute; left: 173px; top: 198px; color: var(--white); font-size: 11px; line-height: 14px; white-space: nowrap; }
  .contact__label { color: var(--blue); }

  .slogan, .offer {
    position: absolute; left: 0; right: 0; text-align: center;
    font-style: italic; font-weight: 700; font-size: 15px; color: var(--blue);
  }
  .slogan { top: 34px; }
  .offer { top: 250px; }
  .card--back-blue .slogan, .card--back-blue .offer { color: var(--white); }
  .back-mark { position: absolute; left: 194px; top: 110px; width: 70px; height: 70px; background: var(--blue); }
  .card--back-blue .back-mark { background: var(--card-black); }
</style>
</head>
<body>

  <section class="card card--front-swoosh">
    <div class="swoosh-area" role="img" aria-label="Decorative blue swoosh arrow leading to the company name"></div>
    <div class="brand"><span class="brand__mark"></span><span class="brand__name">BELLWIN</span></div>
    <div class="person">
      <div class="person__name">Marcus Bellwin</div>
      <div class="person__title">Managing Partner</div>
    </div>
    <div class="contact">
      8734 Fernhollow Ave. Suite 4580<br>
      Los Angeles, CA 90217<br>
      <span class="contact__label">Phone :</span> 323.555.0148<br>
      <span class="contact__label">Fax :</span> 323-555-0172<br>
      <span class="contact__label">Email :</span> marcus@orlaridgecapital.example<br>
      <span class="contact__label">Web :</span> orlaridgecapital.example
    </div>
  </section>

  <section class="card card--front-plain">
    <div class="brand"><span class="brand__mark"></span><span class="brand__name">BELLWIN</span></div>
    <div class="person">
      <div class="person__name">Marcus Bellwin</div>
      <div class="person__title">Managing Partner</div>
    </div>
    <div class="contact">
      8734 Fernhollow Ave. Suite 4580<br>
      Los Angeles, CA 90217<br>
      <span class="contact__label">Phone :</span> 323.555.0148<br>
      <span class="contact__label">Fax :</span> 323-555-0172<br>
      <span class="contact__label">Email :</span> marcus@orlaridgecapital.example<br>
      <span class="contact__label">Web :</span> orlaridgecapital.example
    </div>
  </section>

  <section class="card card--back-dark">
    <p class="slogan">Hedge Fund Strategies at Mutual Fund Prices</p>
    <span class="back-mark"></span>
    <p class="offer">Free Financial Check-Up</p>
  </section>

  <section class="card card--back-blue">
    <p class="slogan">Hedge Fund Strategies at Mutual Fund Prices</p>
    <span class="back-mark"></span>
    <p class="offer">Free Financial Check-Up</p>
  </section>

</body>
</html>
```